Business Card for beauty technology startup

Design Glowmi Business Card for a Beauty, based on the website identity and colors (https://www.glowmi-example.com).
Glowmi is a beauty tech startup that gathers helpful product info for beauty lovers and consumers (such as availability on stores, price range and product reviews) for makeup products. The card design must be young, colorful but clean, and very modern.

Target Market(s)

woman, 15-35

Industry/Entity Type

Cosmetics

Contact Information for Business Card

Full Name, address, phone

Font styles to use
Other font styles liked:
• Advent Pro

Colors
e34297
86cfc6
ffffff
5c5c5c
e8e8e8
e667a6
b2b2b2

Requirements
Must have
• One full colored side with a creative design and another with card info
• Use Color palette: #95C5C5 and/or #D38AA5
• Use fonts: Advent Pro
• Use website identity: https://www.glowmi-example.com
Nice to have
• If needed extra font: Roboto

```html
<!DOCTYPE html>
<html lang="en">
<head>
<meta charset="utf-8">
<title>Glowmi Business Card</title>
<link href="https://fonts.googleapis.com/css2?family=Advent+Pro:wght@300;400&display=swap" rel="stylesheet">
<style>
  :root {
    --backdrop: #ece2d6;
    --teal: #95c5bd;
    --teal-deep: #6fa8a2;
    --teal-mid: #82bcb7;
    --teal-light: #b2d6d0;
    --pink: #e34297;
    --pink-soft: #eeaccb;
    --pink-pale: #f3c9dc;
    --white: #ffffff;
  }
  * { margin: 0; padding: 0; box-sizing: border-box; }
  html, body { width: 1200px; height: 1088px; overflow: hidden; }
  body {
    background: var(--backdrop);
    font-family: "Advent Pro", sans-serif;
    position: relative;
  }
  .card {
    position: absolute;
    left: 170px;
    width: 860px;
    height: 480px;
    background: var(--teal);
    overflow: hidden;
    box-shadow: 0 2px 6px rgba(90, 70, 50, 0.18);
  }
  .card-front { top: 48px; }
  .card-back { top: 560px; }

  .flower-area {
    position: absolute;
    left: -190px;
    top: 90px;
    width: 420px;
    height: 380px;
    border-radius: 50%;
    background: radial-gradient(circle at 35% 50%, var(--pink-soft) 0%, var(--pink-pale) 70%, rgba(243, 201, 220, 0) 72%);
  }

  .brand {
    position: absolute;
    display: flex;
    align-items: center;
    gap: 18px;
  }
  .brand-dot {
    width: 44px;
    height: 44px;
    border-radius: 50%;
    border: 2px solid currentColor;
  }
  .brand-name {
    font-weight: 300;
    letter-spacing: 0.18em;
    text-transform: uppercase;
  }
  .card-front .brand {
    left: 276px;
    top: 200px;
    color: var(--white);
  }
  .card-front .brand-name { font-size: 40px; }

  .back-curves {
    position: absolute;
    inset: 0;
    width: 100%;
    height: 100%;
  }
  .card-back .brand {
    left: 104px;
    top: 262px;
    color: var(--pink);
  }
  .card-back .brand-name { font-size: 48px; }

  .contact-list {
    position: absolute;
    left: 216px;
    top: 334px;
    list-style: none;
    color: var(--white);
    font-weight: 300;
    font-size: 22px;
  }
  .contact-item {
    display: flex;
    align-items: center;
    gap: 14px;
    height: 33px;
  }
  .contact-icon {
    width: 24px;
    height: 24px;
    flex: none;
  }
</style>
</head>
<body>

<section class="card card-front">
  <div class="flower-area" role="img" aria-label="Pink lotus flower illustration"></div>
  <div class="brand">
    <span class="brand-dot"></span>
    <span class="brand-name">Glowmi</span>
  </div>
</section>

<section class="card card-back">
  <svg class="back-curves" viewBox="0 0 860 480" preserveAspectRatio="none" aria-hidden="true">
    <path d="M640 0 C760 60 840 200 830 300 C820 380 740 450 640 480 L860 480 L860 0 Z" fill="var(--teal-light)" opacity="0.55"/>
    <path d="M700 0 C800 90 840 220 800 330 C770 410 700 460 620 480 L860 480 L860 0 Z" fill="var(--teal-mid)" opacity="0.7"/>
    <path d="M860 250 C820 360 740 440 650 480 L860 480 Z" fill="var(--teal-deep)"/>
  </svg>

  <div class="brand">
    <span class="brand-dot"></span>
    <span class="brand-name">Glowmi</span>
  </div>

  <ul class="contact-list">
    <li class="contact-item">
      <svg class="contact-icon" viewBox="0 0 24 24" fill="none" stroke="#fff" stroke-width="1.4"><circle cx="12" cy="12" r="10"/><circle cx="12" cy="10" r="3"/><path d="M7 17c1.5-2.5 8.5-2.5 10 0"/></svg>
      <span>/glowmi.studio</span>
    </li>
    <li class="contact-item">
      <svg class="contact-icon" viewBox="0 0 24 24" fill="none" stroke="#fff" stroke-width="1.4"><circle cx="12" cy="12" r="10"/><path d="M12 18s-4-4.5-4-7.5a4 4 0 0 1 8 0c0 3-4 7.5-4 7.5z"/><circle cx="12" cy="10.5" r="1.4"/></svg>
      <span>/48 Lotus Lane, Hoa Binh, Vietnam</span>
    </li>
    <li class="contact-item">
      <svg class="contact-icon" viewBox="0 0 24 24" fill="none" stroke="#fff" stroke-width="1.4"><circle cx="12" cy="12" r="10"/><path d="M8.5 7.5l2 2-1.2 1.4a7 7 0 0 0 3.8 3.8l1.4-1.2 2 2-1.3 1.3c-3.5 0-8-4.5-8-8z"/></svg>
      <span>/+84 555 0142 889</span>
    </li>
    <li class="contact-item">
      <svg class="contact-icon" viewBox="0 0 24 24" fill="none" stroke="#fff" stroke-width="1.4"><circle cx="12" cy="12" r="10"/><circle cx="12" cy="12" r="5.5"/><path d="M6.5 12h11M12 6.5c-2 3-2 8 0 11M12 6.5c2 3 2 8 0 11"/></svg>
      <span>/www.glowmi-example.com</span>
    </li>
  </ul>
</section>

</body>
</html>
```